Financial Services Company power point theme design

We need a PowerPoint theme designed for client presentations and company orientations. We do like modern designs using blue colors. attached is our logos the logo colors may change as needed to fit the theme. Landscape 16: 9 is acceptable

Industry/Entity Type

Financial Service

Colors

Designer to choose colors to be used in the design.

```html
<!DOCTYPE html>
<html lang="en">
<head>
<meta charset="utf-8">
<title>Keystone Ridge Financial – Presentation Theme</title>
<link rel="stylesheet" href="https://fonts.googleapis.com/css2?family=Merriweather:wght@700;900&family=Open+Sans:wght@400;600;700&display=swap">
<style>
  :root{
    --navy:#1b3564;
    --navy-deep:#142a52;
    --navy-soft:#2f4f86;
    --grey:#8c8c8c;
    --grey-light:#d9dde3;
    --ink:#2b2b2b;
    --canvas:#eef0f3;
    --white:#ffffff;
    --photo-a:#8a94a6;
    --photo-b:#c9ced6;
  }
  *{box-sizing:border-box;margin:0;padding:0}
  html,body{width:993px;height:1200px;overflow:hidden;background:var(--canvas)}
  .canvas{position:relative;width:993px;height:1200px;overflow:hidden;background:var(--canvas);font-family:'Open Sans',sans-serif;color:var(--ink)}
  .slide{position:absolute;width:296px;height:223px;background:var(--white);overflow:hidden;box-shadow:0 1px 4px rgba(20,30,60,.18)}
  .slide--navy{background:var(--navy)}
  .abs{position:absolute}
  .photo{position:absolute;background:linear-gradient(135deg,var(--photo-a),var(--photo-b))}
  .photo--blue{background:linear-gradient(135deg,#3a5787,#8fa3c4)}
  .photo--warm{background:linear-gradient(135deg,#8d7a6b,#d8ccc0)}

  /* brand */
  .brand{position:absolute;display:flex;align-items:center;gap:4px;font-family:'Merriweather',serif;font-weight:700;color:var(--navy);line-height:1.1}
  .brand__mark{width:12px;height:12px;background:var(--navy);flex:none}
  .brand__name{font-size:6.5px;letter-spacing:.2px}
  .brand--light{color:var(--white)}
  .brand--light .brand__mark{background:var(--white)}
  .brand--big .brand__mark{width:17px;height:17px}
  .brand--big .brand__name{font-size:8.5px}

  /* titles */
  .cover-title{position:absolute;left:12px;font-family:'Merriweather',serif;font-weight:700;font-size:13.5px;color:var(--navy);letter-spacing:.2px}
  .cover-sub{position:absolute;left:12px;font-family:'Merriweather',serif;font-weight:700;font-size:7.5px;color:var(--navy)}
  .light{color:var(--white)}
  .hd{position:absolute;left:0;top:14px;padding-left:20px;font-family:'Merriweather',serif;font-weight:700;font-size:11px;color:var(--navy);letter-spacing:.2px;line-height:14px}
  .hd::before{content:"";position:absolute;left:0;top:0;border-left:8px solid var(--navy);border-top:7px solid transparent;border-bottom:7px solid transparent}
  .hd--light{color:var(--white)}
  .hd--light::before{border-left-color:var(--white)}

  .txt{position:absolute;font-size:5.3px;line-height:1.4;color:var(--ink)}
  .txt p+p{margin-top:5px}
  .txt--light{color:var(--white)}
  .lead{font-weight:700}
  .sub{position:absolute;font-family:'Open Sans',sans-serif;font-weight:700;font-size:6.5px;color:var(--navy)}
  .label{font-weight:700;font-size:6px;color:var(--navy);margin-bottom:2px}
  .label--light{color:var(--white);font-size:7.5px;font-family:'Merriweather',serif}

  /* footer */
  .foot-brand{position:absolute;left:16px;bottom:4px;display:flex;align-items:center;gap:2px;font-family:'Merriweather',serif;font-weight:700;font-size:3.6px;color:var(--navy);line-height:1.05}
  .foot-brand i{display:block;width:6px;height:6px;background:var(--navy)}
  .foot-brand--light{color:var(--white)}
  .foot-brand--light i{background:var(--white)}
  .foot-bar{position:absolute;left:84px;right:24px;bottom:0;height:8px;background:var(--navy);clip-path:polygon(6px 0,100% 0,100% 100%,0 100%)}
  .foot-bar::after{content:"";position:absolute;right:0;top:0;width:8px;height:8px;background:var(--white);clip-path:polygon(100% 0,100% 100%,0 100%)}
  .page-no{position:absolute;right:8px;bottom:1px;font-size:6.5px;font-weight:700;color:var(--navy)}
  .page-no--light{color:var(--white)}

  ul.bullets{list-style:none}
  ul.bullets li{position:relative;padding-left:7px;font-size:5.3px;line-height:1.9}
  ul.bullets li::before{content:"";position:absolute;left:0;top:3.6px;width:3px;height:3px;background:var(--navy)}

  .step{position:absolute;width:22px;height:22px;border-radius:50%;background:var(--navy);color:var(--white);font-size:8px;font-weight:700;display:flex;align-items:center;justify-content:center;border:2px solid var(--white);box-shadow:0 0 0 1px var(--grey-light)}
  .step--grey{background:var(--grey)}
  .icon-row{display:flex;align-items:center;gap:5px;font-size:5px;line-height:1;margin-bottom:5px}
  .icon-row svg{flex:none}
</style>
</head>
<body>
<main class="canvas">

  <!-- 1 Cover, white with collage -->
  <section class="slide" style="left:35px;top:19px">
    <div class="brand" style="left:12px;top:34px"><span class="brand__mark"></span><span class="brand__name">KEYSTONE RIDGE<br>FINANCIAL LLC.</span></div>
    <h1 class="cover-title" style="top:108px">PRESENTATION TITLE</h1>
    <p class="cover-sub" style="top:127px">Presentation Subtitle Goes Here</p>
    <svg class="abs" style="left:118px;top:128px" width="178" height="95" viewBox="0 0 178 95" role="img" aria-label="Collage of client and team photographs in slanted tiles">
      <defs><linearGradient id="ph1" x1="0" y1="0" x2="1" y2="1"><stop offset="0" stop-color="#9aa3b2"/><stop offset="1" stop-color="#d6d9df"/></linearGradient></defs>
      <polygon points="120,0 178,-10 178,18 128,28" fill="url(#ph1)"/>
      <polygon points="62,18 116,8 124,36 70,46" fill="url(#ph1)"/>
      <polygon points="126,34 178,24 178,56 134,64" fill="var(--navy)"/>
      <polygon points="20,48 64,40 70,64 26,72" fill="var(--navy)"/>
      <polygon points="72,48 126,38 134,68 80,78" fill="url(#ph1)"/>
      <polygon points="138,66 178,58 178,95 146,95" fill="url(#ph1)"/>
      <polygon points="30,78 74,70 80,95 34,95" fill="url(#ph1)"/>
      <polygon points="84,82 136,72 142,95 88,95" fill="var(--navy)"/>
    </svg>
  </section>

  <!-- 2 Cover, navy with portrait -->
  <section class="slide slide--navy" style="left:352px;top:19px">
    <svg class="abs" style="left:0;top:0" width="296" height="223" viewBox="0 0 296 223" aria-hidden="true">
      <polygon points="60,223 120,160 190,160 130,223" fill="#ffffff" fill-opacity=".06"/>
      <polygon points="130,150 170,110 230,110 190,150" fill="#ffffff" fill-opacity=".05"/>
    </svg>
    <div class="photo photo--warm" style="left:178px;top:0;width:118px;height:223px" role="img" aria-label="Smiling consultant on the phone holding a tablet"></div>
    <div class="brand brand--light" style="left:12px;top:34px"><span class="brand__mark"></span><span class="brand__name">KEYSTONE RIDGE<br>FINANCIAL LLC.</span></div>
    <h1 class="cover-title light" style="top:106px">PRESENTATION TITLE</h1>
    <p class="cover-sub light" style="top:125px">Presentation Subtitle Goes Here</p>
  </section>

  <!-- 3 Cover, white with shapes -->
  <section class="slide" style="left:669px;top:19px">
    <div class="brand" style="left:12px;top:34px"><span class="brand__mark"></span><span class="brand__name">KEYSTONE RIDGE<br>FINANCIAL LLC.</span></div>
    <h1 class="cover-title" style="top:104px">PRESENTATION TITLE</h1>
    <p class="cover-sub" style="top:123px">Presentation Subtitle Goes Here</p>
    <svg class="abs" style="left:130px;top:140px" width="166" height="83" viewBox="0 0 166 83" aria-hidden="true">
      <polygon points="18,28 104,6 128,40 42,62" fill="var(--navy)"/>
      <polygon points="118,8 160,0 166,0 166,24 134,32" fill="var(--navy)"/>
      <polygon points="80,72 146,56 166,66 166,83 96,83" fill="var(--navy)"/>
    </svg>
  </section>

  <!-- 4 Welcome -->
  <section class="slide" style="left:35px;top:251px">
    <h2 class="hd" style="top:46px">WELCOME MESSAGE</h2>
    <div class="txt" style="left:20px;top:76px;width:134px">
      <p>Lorem ipsum dolor sit amet, consectetur adipiscing elit, sed do eiusmod tempor incididunt ut labore et dolore magna aliqua. Ut enim ad minim veniam, quis nostrud exercitation ullamco laboris nisi ut aliquip ex ea commodo consequat.</p>
      <p>Duis aute irure dolor in reprehenderit in voluptate velit esse cillum dolore eu fugiat nulla pariatur reprehenderit.</p>
    </div>
    <div class="photo photo--warm" style="left:164px;top:0;width:132px;height:223px" role="img" aria-label="Smiling businesswoman shaking hands with a client"></div>
    <div class="foot-brand"><i></i><span>KEYSTONE RIDGE<br>FINANCIAL LLC.</span></div>
    <div class="foot-bar" style="right:132px"></div>
  </section>

  <!-- 5 Heading -->
  <section class="slide" style="left:352px;top:251px">
    <h2 class="hd" style="top:14px">HEADING GOES HERE</h2>
    <p class="sub" style="left:26px;top:50px">SUBHEADING GOES HERE</p>
    <div class="txt" style="left:26px;top:63px;width:250px">
      <p>Lorem ipsum dolor sit amet, consectetur adipiscing elit, sed do eiusmod tempor incididunt ut labore et dolore magna aliqua. Ut enim ad minim veniam, quis nostrud exercitation ullamco laboris nisi ut aliquip ex ea commodo consequat. Duis aute irure dolor in reprehenderit in voluptate velit esse cillum dolore eu fugiat nulla pariatur.</p>
      <p>Lorem ipsum dolor sit amet, consectetur adipiscing elit, sed do eiusmod tempor incididunt ut labore et dolore magna aliqua. Ut enim ad minim veniam, quis nostrud exercitation ullamco laboris nisi ut aliquip ex ea commodo consequat. Duis aute irure dolor in reprehenderit in voluptate velit esse cillum dolore eu fugiat nulla pariatur.</p>
    </div>
    <div class="foot-brand"><i></i><span>KEYSTONE RIDGE<br>FINANCIAL LLC.</span></div>
    <div class="foot-bar"></div><span class="page-no">13</span>
  </section>

  <!-- 6 Tagline and steps -->
  <section class="slide" style="left:669px;top:251px">
    <div class="photo photo--blue" style="left:0;top:0;width:296px;height:100px" role="img" aria-label="Advisors reviewing documents at a desk, blue tinted"></div>
    <p class="abs" style="left:16px;top:16px;font-family:'Open Sans',sans-serif;font-weight:600;font-size:11px;color:var(--white);letter-spacing:.3px">ALWAYS IN YOUR CORNER</p>
    <p class="abs" style="left:16px;top:31px;font-size:5px;color:var(--white);opacity:.8">FOR YOUR FAMILY AND YOUR BUSINESS</p>
    <div class="step" style="left:44px;top:89px">1</div>
    <div class="step" style="left:136px;top:89px">2</div>
    <div class="step step--grey" style="left:226px;top:89px">3</div>
    <div class="txt" style="left:34px;top:120px;width:64px"><p class="label">TEXT GOES HERE</p>Lorem ipsum dolor sit amet, consectetur adipiscing elit sed do.</div>
    <div class="txt" style="left:126px;top:120px;width:64px"><p class="label">TEXT GOES HERE</p>Lorem ipsum dolor sit amet, consectetur adipiscing elit sed do.</div>
    <div class="txt" style="left:216px;top:120px;width:64px"><p class="label">TEXT GOES HERE</p>Lorem ipsum dolor sit amet, consectetur adipiscing elit sed do.</div>
    <div class="foot-brand"><i></i><span>KEYSTONE RIDGE<br>FINANCIAL LLC.</span></div>
    <div class="foot-bar"></div><span class="page-no">13</span>
  </section>

  <!-- 7 Text, picture and bullets -->
  <section class="slide" style="left:35px;top:485px">
    <h2 class="hd">TEXT, PICTURE AND BULLETS</h2>
    <div class="txt" style="left:20px;top:36px;width:262px">
      <p><span class="lead">Lorem ipsum dolor sit amet, consectetur adipiscing elit, sed do eiusmod tempor incididunt ut labore et dolore magna aliqua. Ut enim ad minim veniam,</span> quis nostrud exercitation ullamco laboris nisi ut aliquip ex ea commodo consequat. Duis aute irure dolor in reprehenderit in voluptate velit esse cillum dolore eu fugiat nulla pariatur.</p>
    </div>
    <div class="abs" style="left:40px;top:112px;width:9px;height:60px;background:var(--navy)"></div>
    <div class="abs" style="left:40px;top:163px;width:60px;height:9px;background:var(--navy)"></div>
    <div class="photo photo--warm" style="left:52px;top:120px;width:54px;height:40px" role="img" aria-label="Family planning finances together"></div>
    <ul class="bullets abs" style="left:150px;top:112px">
      <li>Lorem ipsum dolor sit amet</li>
      <li>Ut enim ad minim veniam</li>
      <li>Incididunt ut labore et dolore magna</li>
      <li>Esse cillum dolore eu fugiat nulla pariatur</li>
      <li>Dolor in reprehenderit in voluptate</li>
      <li>Nisi ut aliquip ex ea</li>
    </ul>
    <div class="foot-brand"><i></i><span>KEYSTONE RIDGE<br>FINANCIAL LLC.</span></div>
    <div class="foot-bar"></div><span class="page-no">13</span>
  </section>

  <!-- 8 Our team -->
  <section class="slide" style="left:352px;top:485px">
    <h2 class="hd">OUR TEAM</h2>
    <div class="photo" style="left:22px;top:48px;width:28px;height:28px;outline:1px solid var(--navy);outline-offset:1px" role="img" aria-label="Team member portrait"></div>
    <div class="photo" style="left:115px;top:48px;width:28px;height:28px;outline:1px solid var(--navy);outline-offset:1px" role="img" aria-label="Team member portrait"></div>
    <div class="photo" style="left:208px;top:48px;width:28px;height:28px;outline:1px solid var(--navy);outline-offset:1px" role="img" aria-label="Team member portrait"></div>
    <div class="txt" style="left:22px;top:84px;width:72px"><p class="label" style="font-size:6.5px">Jonathan Doe</p>Lorem ipsum dolor sit amet, consectetur adipiscing elit, sed do eiusmod tempor incididunt ut labore et dolore magna aliqua.<p>Ut enim ad minim veniam, quis nostrud exercitation ullamco laboris nisi ut aliquip ex ea.</p></div>
    <div class="txt" style="left:115px;top:84px;width:72px"><p class="label" style="font-size:6.5px">Jonathan Doe</p>Lorem ipsum dolor sit amet, consectetur adipiscing elit, sed do eiusmod tempor incididunt ut labore et dolore magna aliqua.<p>Ut enim ad minim veniam, quis nostrud exercitation ullamco laboris nisi ut aliquip ex ea.</p></div>
    <div class="txt" style="left:208px;top:84px;width:72px"><p class="label" style="font-size:6.5px">Jonathan Doe</p>Lorem ipsum dolor sit amet, consectetur adipiscing elit, sed do eiusmod tempor incididunt ut labore et dolore magna aliqua.<p>Ut enim ad minim veniam, quis nostrud exercitation ullamco laboris nisi ut aliquip ex ea.</p></div>
    <div class="foot-brand"><i></i><span>KEYSTONE RIDGE<br>FINANCIAL LLC.</span></div>
    <div class="foot-bar"></div><span class="page-no">13</span>
  </section>

  <!-- 9 Blue background -->
  <section class="slide slide--navy" style="left:669px;top:485px">
    <div class="abs" style="left:110px;top:140px;width:186px;height:70px;background:linear-gradient(90deg,rgba(27,53,100,0),#3d5c90 60%,#4b6a9c);opacity:.8" role="img" aria-label="Faded photo of a team meeting"></div>
    <h2 class="hd hd--light">BLUE BACKGROUND SLIDE</h2>
    <svg class="abs" style="left:20px;top:62px" width="10" height="10" viewBox="0 0 10 10" aria-hidden="true"><path d="M5 0 L10 3 H0 Z M1 4 H2.5 V8 H1 Z M4.2 4 H5.8 V8 H4.2 Z M7.5 4 H9 V8 H7.5 Z M0 9 H10 V10 H0 Z" fill="#fff"/></svg>
    <svg class="abs" style="left:158px;top:62px" width="10" height="10" viewBox="0 0 10 10" aria-hidden="true"><path d="M0 10 V6 H2 V10 Z M3 10 V4 H5 V10 Z M6 10 V2 H8 V10 Z M1 4 L4 1.5 L6 3 L9 0" stroke="#fff" stroke-width=".8" fill="#fff"/></svg>
    <div class="txt txt--light" style="left:20px;top:77px;width:118px"><p class="label label--light">PLACE TITLE TEXT</p>Lorem ipsum dolor sit amet, consectetur adipiscing elit, sed do eiusmod tempor incididunt ut labore et dolore magna aliqua. Ut enim ad minim veniam, quis nostrud exercitation ullamco laboris nisi ut aliquip ex ea commodo consequat. Duis aute irure dolor in reprehenderit in voluptate velit esse cillum dolore eu fugiat nulla pariatur.</div>
    <div class="txt txt--light" style="left:158px;top:77px;width:118px"><p class="label label--light">PLACE TITLE TEXT</p>Lorem ipsum dolor sit amet, consectetur adipiscing elit, sed do eiusmod tempor incididunt ut labore et dolore magna aliqua. Ut enim ad minim veniam, quis nostrud exercitation ullamco laboris nisi ut aliquip ex ea commodo consequat. Duis aute irure dolor in reprehenderit in voluptate velit esse cillum dolore eu fugiat nulla pariatur.</div>
    <div class="foot-brand foot-brand--light"><i></i><span>KEYSTONE RIDGE<br>FINANCIAL LLC.</span></div>
    <div class="foot-bar" style="background:var(--white);clip-path:none;height:6px;left:84px;right:0"></div>
    <span class="page-no" style="color:var(--navy);bottom:-1px;font-size:5.5px">13</span>
  </section>

  <!-- 10 Graphs and charts -->
  <section class="slide" style="left:35px;top:717px">
    <h2 class="hd">GRAPHS AND CHARTS</h2>
    <svg class="abs" style="left:34px;top:40px" width="110" height="62" viewBox="0 0 110 62" role="img" aria-label="Horizontal bar chart">
      <g font-size="3.5" fill="#777" font-family="Open Sans,sans-serif">
        <text x="0" y="8">2017</text><text x="0" y="20">2016</text><text x="0" y="32">2015</text><text x="0" y="44">2014</text>
      </g>
      <line x1="12" y1="0" x2="12" y2="50" stroke="#ccc" stroke-width=".4"/>
      <g fill="#cfd4dc"><rect x="12" y="2" width="82" height="3"/><rect x="12" y="14" width="70" height="3"/><rect x="12" y="26" width="88" height="3"/><rect x="12" y="38" width="64" height="3"/></g>
      <g fill="var(--navy)"><rect x="12" y="6" width="60" height="3"/><rect x="12" y="18" width="78" height="3"/><rect x="12" y="30" width="50" height="3"/><rect x="12" y="42" width="72" height="3"/></g>
      <g font-size="3.2" fill="#777" font-family="Open Sans,sans-serif"><text x="12" y="56">0</text><text x="34" y="56">200</text><text x="56" y="56">400</text><text x="78" y="56">600</text><text x="98" y="56">800</text></g>
    </svg>
    <div class="txt" style="left:150px;top:44px;width:70px"><p class="label"><span style="display:inline-block;width:4px;height:4px;background:var(--navy);margin-right:3px"></span>Title Text</p>Lorem ipsum dolor sit amet, consectetur adipiscing elit sed do.</div>
    <div class="txt" style="left:150px;top:78px;width:70px"><p class="label"><span style="display:inline-block;width:4px;height:4px;background:var(--navy);margin-right:3px"></span>Title Text</p>Lorem ipsum dolor sit amet, consectetur adipiscing elit sed do.</div>
    <svg class="abs" style="left:34px;top:136px" width="40" height="40" viewBox="-20 -20 40 40" role="img" aria-label="Pie chart">
      <circle r="18" fill="var(--navy)"/>
      <path d="M0 0 L0 -18 A18 18 0 0 1 17.1 -5.6 Z" fill="#5a7bb5"/>
      <path d="M0 0 L-15.6 9 A18 18 0 0 1 -12.7 -12.7 Z" fill="var(--grey)"/>
    </svg>
    <div class="txt" style="left:82px;top:145px;width:196px"><p class="lead">Lorem ipsum dolor sit amet, consectetur adipiscing elit, sed do eiusmod tempor incididunt ut labore et dolore magna aliqua. Ut enim ad minim veniam, quis nostrud exercitation ullamco laboris nisi ut aliquip ex ea commodo consequat.</p></div>
    <div class="foot-brand"><i></i><span>KEYSTONE RIDGE<br>FINANCIAL LLC.</span></div>
    <div class="foot-bar"></div><span class="page-no">13</span>
  </section>

  <!-- 11 Image and text -->
  <section class="slide" style="left:352px;top:717px">
    <h2 class="hd">IMAGE AND TEXT SLIDE</h2>
    <div class="photo" style="left:0;top:54px;width:158px;height:148px;background:linear-gradient(160deg,#b7c3cf,#8a7a66 55%,#5c6b4f)" role="img" aria-label="Office tower with palm trees"></div>
    <div class="abs" style="left:158px;top:54px;width:138px;height:148px;background:var(--navy)"></div>
    <div class="txt txt--light" style="left:172px;top:98px;width:112px"><p class="label label--light">PLACE TITLE TEXT</p>Lorem ipsum dolor sit amet, consectetur adipiscing elit, sed do eiusmod tempor incididunt ut labore et dolore magna aliqua. Ut enim ad minim veniam, quis nostrud exercitation ullamco laboris nisi ut aliquip ex ea commodo consequat. Duis aute irure dolor in reprehenderit in voluptate velit esse cillum dolore.</div>
    <div class="foot-brand"><i></i><span>KEYSTONE RIDGE<br>FINANCIAL LLC.</span></div>
    <div class="foot-bar"></div><span class="page-no">13</span>
  </section>

  <!-- 12 Our process -->
  <section class="slide" style="left:669px;top:717px">
    <h2 class="hd">OUR PROCESS</h2>
    <svg class="abs" style="left:108px;top:80px" width="80" height="64" viewBox="-40 -32 80 64" aria-hidden="true">
      <g fill="var(--navy)" stroke="#fff" stroke-width="1.5">
        <path d="M0 -30 A30 30 0 0 1 30 0 L17 0 A17 17 0 0 0 0 -17 Z"/>
        <path d="M30 0 A30 30 0 0 1 0 30 L0 17 A17 17 0 0 0 17 0 Z"/>
        <path d="M0 30 A30 30 0 0 1 -30 0 L-17 0 A17 17 0 0 0 0 17 Z"/>
        <path d="M-30 0 A30 30 0 0 1 0 -30 L0 -17 A17 17 0 0 0 -17 0 Z"/>
      </g>
      <circle r="14" fill="#fff" stroke="var(--navy)" stroke-width="1"/>
      <rect x="-5" y="-5" width="10" height="10" fill="var(--navy)"/>
      <g stroke="#9aa6b8" stroke-width=".6" fill="none">
        <path d="M-25 -18 L-36 -28"/><path d="M25 -18 L36 -28"/><path d="M-25 18 L-36 28"/><path d="M25 18 L36 28"/>
      </g>
    </svg>
    <div class="txt" style="left:14px;top:56px;width:78px"><p class="label" style="font-size:6.5px">Text Title</p>Lorem ipsum dolor sit amet, consectetur adipiscing elit, sed do eiusmod tempor incididunt ut labore et dolore</div>
    <div class="txt" style="left:204px;top:56px;width:78px;text-align:left"><p class="label" style="font-size:6.5px">Text Title</p>Lorem ipsum dolor sit amet, consectetur adipiscing elit, sed do eiusmod tempor incididunt ut labore et dolore</div>
    <div class="txt" style="left:14px;top:144px;width:78px"><p class="label" style="font-size:6.5px">Text Title</p>Lorem ipsum dolor sit amet, consectetur adipiscing elit, sed do eiusmod tempor incididunt ut labore et dolore</div>
    <div class="txt" style="left:204px;top:144px;width:78px"><p class="label" style="font-size:6.5px">Text Title</p>Lorem ipsum dolor sit amet, consectetur adipiscing elit, sed do eiusmod tempor incididunt ut labore et dolore</div>
    <div class="foot-brand"><i></i><span>KEYSTONE RIDGE<br>FINANCIAL LLC.</span></div>
    <div class="foot-bar"></div><span class="page-no">13</span>
  </section>

  <!-- 13 Chart slide -->
  <section class="slide" style="left:35px;top:950px">
    <h2 class="hd">CHART SLIDE</h2>
    <svg class="abs" style="left:22px;top:46px" width="114" height="120" viewBox="0 0 114 120" role="img" aria-label="Vertical bar chart by category">
      <rect x=".5" y=".5" width="113" height="100" fill="none" stroke="#ddd" stroke-width=".5"/>
      <line x1="8" y1="86" x2="108" y2="86" stroke="#bbb" stroke-width=".4"/>
      <g fill="var(--navy)"><rect x="14" y="48" width="4" height="38"/><rect x="38" y="40" width="4" height="46"/><rect x="62" y="44" width="4" height="42"/><rect x="86" y="24" width="4" height="62"/></g>
      <g fill="#4f6fa8"><rect x="19" y="62" width="4" height="24"/><rect x="43" y="58" width="4" height="28"/><rect x="67" y="56" width="4" height="30"/><rect x="91" y="50" width="4" height="36"/></g>
      <g fill="var(--grey)"><rect x="24" y="70" width="4" height="16"/><rect x="48" y="66" width="4" height="20"/><rect x="72" y="62" width="4" height="24"/><rect x="96" y="40" width="4" height="46"/></g>
      <g font-size="3.2" fill="#666" font-family="Open Sans,sans-serif"><text x="10" y="93">Category 1</text><text x="34" y="93">Category 2</text><text x="58" y="93">Category 3</text><text x="82" y="93">Category 4</text></g>
      <g font-size="4" fill="var(--navy)" font-family="Open Sans,sans-serif" font-weight="700">
        <rect x="4" y="112" width="3" height="3"/><text x="9" y="115">Title Text</text>
        <rect x="40" y="112" width="3" height="3" fill="#4f6fa8"/><text x="45" y="115">Title Text</text>
        <rect x="76" y="112" width="3" height="3" fill="#8c8c8c"/><text x="81" y="115">Title Text</text>
      </g>
    </svg>
    <p class="sub" style="left:158px;top:42px">SUBTITLE GOES HERE</p>
    <div class="txt" style="left:158px;top:52px;width:122px">
      <p>Lorem ipsum dolor sit amet, consectetur adipiscing elit, sed do eiusmod tempor incididunt ut labore et dolore magna aliqua. Ut enim ad minim veniam, quis nostrud exercitation ullamco laboris nisi ut aliquip ex ea commodo consequat. Duis aute irure dolor in reprehenderit in voluptate velit esse cillum dolore eu fugiat nulla pariatur. Excepteur sint occaecat cupidatat non proident, sunt in culpa qui officia deserunt mollit anim id est laborum. Sed ut perspiciatis unde omnis iste natus error sit voluptatem accusantium doloremque laudantium, totam rem aperiam, eaque ipsa quae ab illo inventore veritatis et quasi architecto beatae vitae dicta sunt explicabo.</p>
    </div>
    <div class="foot-brand"><i></i><span>KEYSTONE RIDGE<br>FINANCIAL LLC.</span></div>
    <div class="foot-bar"></div><span class="page-no">13</span>
  </section>

  <!-- 14 Why us -->
  <section class="slide" style="left:352px;top:950px">
    <svg class="abs" style="left:110px;top:0" width="186" height="210" viewBox="0 0 186 210" role="img" aria-label="Business handshake over a desk, blue tinted">
      <defs><linearGradient id="ph14" x1="0" y1="0" x2="1" y2="1"><stop offset="0" stop-color="#c3cbd8"/><stop offset=".5" stop-color="#6d80a3"/><stop offset="1" stop-color="#2b4677"/></linearGradient></defs>
      <polygon points="130,0 186,0 186,210 20,210" fill="url(#ph14)"/>
    </svg>
    <h2 class="hd" style="top:14px">WHY US</h2>
    <div class="txt" style="left:20px;top:60px;width:118px">
      <p>Lorem ipsum dolor sit amet, consectetur adipiscing elit, sed do eiusmod tempor incididunt ut labore et dolore magna aliqua. Ut enim ad minim veniam, quis nostrud exercitation ullamco laboris nisi ut aliquip ex ea commodo consequat. Duis aute irure dolor in reprehenderit in voluptate velit esse cillum dolore eu fugiat nulla pariatur.</p>
    </div>
    <div class="foot-brand"><i></i><span>KEYSTONE RIDGE<br>FINANCIAL LLC.</span></div>
    <div class="foot-bar"></div><span class="page-no">13</span>
  </section>

  <!-- 15 Contact -->
  <section class="slide" style="left:669px;top:950px">
    <div class="brand brand--big" style="left:20px;top:28px"><span class="brand__mark"></span><span class="brand__name">KEYSTONE RIDGE<br>FINANCIAL LLC.</span></div>
    <p class="abs" style="left:20px;top:66px;font-family:'Merriweather',serif;font-weight:700;font-size:10px;color:var(--navy)">Contact Us</p>
    <div class="abs" style="left:20px;top:86px">
      <div class="icon-row"><svg width="7" height="7" viewBox="0 0 10 10"><circle cx="5" cy="5" r="4.6" fill="none" stroke="var(--navy)" stroke-width=".8"/><path d="M3.3 2.8 L4.3 2.8 L4.7 4 L4.1 4.5 Q4.8 5.7 5.6 6 L6.1 5.4 L7.2 5.8 L7.2 6.8 Q4.2 7.2 3.3 2.8Z" fill="var(--navy)"/></svg>(555) 014 2290</div>
      <div class="icon-row"><svg width="7" height="7" viewBox="0 0 10 10"><circle cx="5" cy="5" r="4.6" fill="none" stroke="var(--navy)" stroke-width=".8"/><rect x="2.7" y="3.3" width="4.6" height="3.4" fill="none" stroke="var(--navy)" stroke-width=".6"/><path d="M2.7 3.3 L5 5.2 L7.3 3.3" fill="none" stroke="var(--navy)" stroke-width=".6"/></svg>hello@keystoneridgefin.com</div>
      <div class="icon-row"><svg width="7" height="7" viewBox="0 0 10 10"><circle cx="5" cy="5" r="4.6" fill="none" stroke="var(--navy)" stroke-width=".8"/><circle cx="5" cy="5" r="2.4" fill="none" stroke="var(--navy)" stroke-width=".6"/><path d="M2.6 5 H7.4 M5 2.6 V7.4" stroke="var(--navy)" stroke-width=".5"/></svg>www.keystoneridgefin.com</div>
      <div class="icon-row"><svg width="7" height="7" viewBox="0 0 10 10"><circle cx="5" cy="5" r="4.6" fill="none" stroke="var(--navy)" stroke-width=".8"/><path d="M5 7.6 Q3 5.2 3 4.2 A2 2 0 0 1 7 4.2 Q7 5.2 5 7.6Z" fill="var(--navy)"/></svg>Street No., Location</div>
    </div>
    <svg class="abs" style="left:120px;top:120px" width="176" height="103" viewBox="0 0 176 103" aria-hidden="true">
      <polygon points="40,32 98,0 150,30 92,62" fill="var(--navy)"/>
    </svg>
    <div class="abs" style="left:214px;top:168px;width:82px;height:55px;background:linear-gradient(135deg,#e4e7ea,#cdd6dc)" role="img" aria-label="Street map showing office location"></div>
  </section>

</main>
</body>
</html>
```